Business Card design for an International Import Export House

We need a Business Card design for our import export business. We trade in Minerals, Metals, Rice, Sugar, Steel etc.. The design should be minimalistic. It may or may not contain the physical address. In case you want to include the physical address - 418 Verandah Heights, Marlow Sector 9, Harbourton, Kestrel State, India, 480217.

Target Market(s)

Steel Mills or Steel Plants, Factories, Mining businesses, Industrial houses, Government Agencies

Industry/Entity Type

Importer

Contact Information for Business Card

Business Name - Corvane Overseas

Font styles to use
Other font styles liked:
• montserrat

Requirements
Must have
• Ravi Kandola - President
• www.corvaneoverseas.com
• ravi@corvaneoverseas.com
• +91-987-654-3217
Nice to have
• worldwide suppliers of ores

```html
<!DOCTYPE html>
<html lang="en">
<head>
<meta charset="utf-8">
<title>Corvane Overseas — Business Card</title>
<link rel="stylesheet" href="https://fonts.googleapis.com/css2?family=Montserrat:wght@700&family=Bodoni+Moda:wght@400;600&display=swap">
<style>
  :root {
    --backdrop: #e4e4e2;
    --card-white: #f4f4f4;
    --card-grey: #dcdcdc;
    --teal: #3f8fa4;
    --ink: #2a2e31;
    --panel: #262626;
    --tile: #3a3a3a;
    --tile-edge: #1c1c1c;
    --tile-text: #f2f2f2;
  }
  * { box-sizing: border-box; margin: 0; padding: 0; }
  html, body { width: 1200px; height: 919px; overflow: hidden; }
  body {
    background: var(--backdrop);
    display: flex;
    flex-direction: column;
    align-items: center;
    justify-content: center;
    gap: 44px;
  }
  .card {
    width: 700px;
    height: 400px;
    position: relative;
    box-shadow: 0 6px 18px rgba(0,0,0,0.18);
    overflow: hidden;
  }

  /* Brand side */
  .card--brand {
    background: radial-gradient(ellipse at 50% 40%, #ffffff 0%, var(--card-white) 45%, var(--card-grey) 100%);
    display: flex;
    flex-direction: column;
    align-items: center;
    justify-content: center;
    gap: 22px;
  }
  .corner-tab {
    position: absolute;
    width: 18px;
    height: 18px;
    background: var(--teal);
  }
  .corner-tab--top { top: 0; left: 0; }
  .corner-tab--bottom { bottom: 0; right: 0; }
  .brand {
    display: flex;
    align-items: center;
    gap: 14px;
  }
  .brand__dot {
    width: 34px;
    height: 34px;
    border-radius: 50%;
    background: var(--teal);
    flex: none;
  }
  .brand__name {
    font-family: "Montserrat", sans-serif;
    font-weight: 700;
    color: var(--ink);
    text-transform: uppercase;
    letter-spacing: 0.5px;
    white-space: nowrap;
  }
  .card--brand .brand__name { font-size: 38px; }
  .tagline {
    font-family: "Bodoni Moda", serif;
    font-weight: 600;
    font-size: 19px;
    letter-spacing: 2px;
    color: var(--ink);
    text-transform: uppercase;
  }

  /* Contact side */
  .card--contact {
    display: flex;
    background: var(--card-white);
  }
  .contact__identity {
    width: 38%;
    background: radial-gradient(ellipse at 50% 45%, #ffffff 0%, var(--card-white) 55%, var(--card-grey) 100%);
    display: flex;
    align-items: center;
    justify-content: center;
  }
  .contact__identity .brand { flex-direction: column; gap: 12px; }
  .contact__identity .brand__name { font-size: 19px; }
  .contact__identity .brand__dot { width: 40px; height: 40px; }
  .contact__panel {
    flex: 1;
    background: var(--panel);
    padding: 14px 14px 14px 12px;
    display: grid;
    grid-template-columns: 56px 1fr;
    grid-template-rows: 70px 70px 80px 1fr;
    gap: 10px;
  }
  .tile {
    background: var(--tile);
    border: 2px solid var(--tile-edge);
    color: var(--tile-text);
    font-family: "Bodoni Moda", serif;
    display: flex;
    align-items: center;
    justify-content: center;
    text-align: center;
  }
  .tile--icon svg { width: 24px; height: 24px; }
  .tile--phone { font-size: 23px; letter-spacing: 1px; }
  .tile--web { flex-direction: column; font-size: 15px; line-height: 1.35; letter-spacing: 0.5px; }
  .tile--address { font-size: 14px; line-height: 1.3; padding: 0 14px; }
  .tile--person {
    grid-column: 1 / span 2;
    flex-direction: column;
    gap: 2px;
  }
  .person__name { font-size: 22px; letter-spacing: 3px; text-transform: uppercase; }
  .person__role { font-size: 13px; letter-spacing: 1.5px; text-transform: uppercase; }
</style>
</head>
<body>

  <section class="card card--brand" aria-label="Card back">
    <span class="corner-tab corner-tab--top"></span>
    <span class="corner-tab corner-tab--bottom"></span>
    <div class="brand">
      <span class="brand__dot"></span>
      <span class="brand__name">Corvane Overseas</span>
    </div>
    <p class="tagline">Worldwide Suppliers of Ores</p>
  </section>

  <section class="card card--contact" aria-label="Card front">
    <div class="contact__identity">
      <div class="brand">
        <span class="brand__dot"></span>
        <span class="brand__name">Corvane Overseas</span>
      </div>
    </div>
    <div class="contact__panel">
      <div class="tile tile--icon" aria-label="Phone">
        <svg viewBox="0 0 24 24" fill="none" stroke="#f2f2f2" stroke-width="1.6">
          <rect x="7" y="2.5" width="10" height="19" rx="1.8"/>
          <line x1="10.5" y1="18.5" x2="13.5" y2="18.5"/>
        </svg>
      </div>
      <div class="tile tile--phone">+91-987-654-3217</div>

      <div class="tile tile--icon" aria-label="Web and email">
        <svg viewBox="0 0 24 24" fill="none" stroke="#f2f2f2" stroke-width="1.6">
          <rect x="7" y="3" width="10" height="18" rx="5"/>
          <line x1="12" y1="6" x2="12" y2="10"/>
        </svg>
      </div>
      <div class="tile tile--web">
        <span>www.corvaneoverseas.com</span>
        <span>ravi@corvaneoverseas.com</span>
      </div>

      <div class="tile tile--icon" aria-label="Address">
        <svg viewBox="0 0 24 24" fill="none" stroke="#f2f2f2" stroke-width="1.6">
          <path d="M12 21s-6-6.2-6-11a6 6 0 0 1 12 0c0 4.8-6 11-6 11z"/>
          <circle cx="12" cy="10" r="2.2"/>
        </svg>
      </div>
      <div class="tile tile--address">418 Verandah Heights, Marlow Sector 9, Harbourton, Kestrel State, India, 480217</div>

      <div class="tile tile--person">
        <span class="person__name">Ravi Kandola</span>
        <span class="person__role">President</span>
      </div>
    </div>
  </section>

</body>
</html>
```